A website design for a consultation firm

We are located in Istanbul, Turkey and offers our consultation services to customers interested in investing in Realestate, Education and Investment particularly this coming from Arab world and English speaking countries.

The site should carry our message of deep knowledge about the Turkish markets in the mentioned sectors of interest, sincerity and keenness.

The final deliverable of the winning design should include:
- The source files of the final designs. e.g. AI, PSD ..etc
- The redline markup for the design using a Specctr or any other similar tool.

Target Market(s)

English and Arabic speaking countries with a Turkish theme since we are a Turkish company

Industry/Entity Type

Consulting

Number of Pages Required

2 page

Font styles to use
Sans Serif

Requirements
Must have
• The site should serve the following main sections:
• - Why QVD?
• - Reports & studies
• - Sectors
• - Our team
• - Contact
• We need a design that could be converted into a WordPress theme.
• The design should be in English but should accommodate other languages including RTL.
• You can use the color theme you like as long as it does't dissolve the logo.
• The site should link into our accounts on the following networks:
• - Updates
• - Community
• - Network
• The design should be responsive and nicely rendered on Desktop, Tablets and Smart phones.
Nice to have
• The site would be nice to balance between being informative and

```html
<!DOCTYPE html>
<html lang="en">
<head>
<meta charset="utf-8">
<title>QVD Consulting</title>
<link href="https://fonts.googleapis.com/css2?family=Raleway:wght@400;600;700&family=Open+Sans:wght@400;600&display=swap" rel="stylesheet">
<style>
:root{
  --red:#d3102a;
  --navy:#0f2d63;
  --navy-deep:#0a1f49;
  --ink:#2b2b2b;
  --muted:#777;
  --grey-bg:#eeeeee;
  --white:#fff;
  --link:#1b4d9b;
  --foot-text:#cfd8ea;
}
*{margin:0;padding:0;box-sizing:border-box}
html,body{width:707px;height:1200px;overflow:hidden;background:var(--white)}
body{position:relative;font-family:"Open Sans",Arial,sans-serif;color:var(--ink)}
.abs{position:absolute}

/* header */
.site-header{left:0;top:0;width:707px;height:68px;background:var(--white)}
.brand-name{left:72px;top:24px;font-family:"Raleway",sans-serif;font-weight:700;font-size:18px;color:var(--navy);line-height:1}
.main-nav{left:300px;top:30px;display:flex;gap:17px;font-family:"Raleway",sans-serif;font-size:8.5px;font-weight:700;color:#555;letter-spacing:.3px}
.main-nav .active{color:var(--navy);border-bottom:2px solid var(--red);padding-bottom:5px}
.lang{left:620px;top:6px;display:flex;gap:5px}
.lang span{width:12px;height:8px;display:block}
.lang .l1{background:var(--red)}
.lang .l2{background:var(--navy)}

/* hero */
.hero{left:0;top:68px;width:707px;height:276px;background:linear-gradient(120deg,#8a9aa8 0%,#c9c2b6 45%,#7d6f66 75%,#3c3a3f 100%)}
.hero-title{left:184px;top:166px;width:340px;height:44px;background:rgba(20,30,55,.72);color:var(--white);font-family:"Raleway",sans-serif;font-weight:700;font-size:24px;letter-spacing:1px;text-align:center;line-height:44px}
.hero-arrow{top:190px;width:24px;height:24px}

/* services band */
.services{left:0;top:344px;width:707px;height:160px;background:var(--red)}
.notch{left:337px;top:503px}
.service{top:320px;width:190px;text-align:center;color:var(--white)}
.service-icon{width:58px;height:58px;margin:0 auto;border-radius:50%;background:var(--white);border:3px solid var(--red);display:flex;align-items:center;justify-content:center}
.service h3{font-family:"Raleway",sans-serif;font-size:10.5px;font-weight:700;line-height:13px;margin-top:9px;letter-spacing:.3px}
.service p{font-size:7.5px;line-height:11px;margin-top:6px;opacity:.9}

/* why */
.why{left:0;top:520px;width:353px;height:238px;background:var(--grey-bg)}
.why-photo{left:353px;top:520px;width:354px;height:238px;background:linear-gradient(110deg,#d9dde0 0%,#b4bcc3 40%,#6e7f93 70%,#c8b7a2 100%)}
.why h2{position:absolute;left:32px;top:30px;font-family:"Raleway",sans-serif;font-size:20px;font-weight:700;color:var(--ink)}
.why p{position:absolute;left:32px;width:290px;font-size:7.5px;line-height:11.5px;color:var(--muted)}
.btn{position:absolute;left:32px;top:182px;width:74px;height:24px;background:var(--navy-deep);color:var(--white);font-family:"Raleway",sans-serif;font-size:8px;font-weight:700;text-align:center;line-height:24px}

/* reports */
.reports-title{left:72px;top:770px;font-family:"Raleway",sans-serif;font-size:17px;font-weight:600;color:var(--navy)}
.reports-rule{left:72px;top:795px;width:563px;height:1px;background:#ddd}
.reports-rule::before{content:"";position:absolute;left:0;top:-1px;width:40px;height:3px;background:var(--red)}
.card{top:808px;width:174px;height:176px;background:var(--white);border:1px solid #e2e2e2}
.card-img{height:88px}
.card h4{font-family:"Raleway",sans-serif;font-size:10.5px;font-weight:600;color:var(--link);margin:9px 8px 4px}
.card p{font-size:7px;line-height:10px;color:var(--muted);margin:0 8px}
.card .more{display:block;margin:6px 8px;font-size:7px;font-weight:600;color:var(--ink)}

/* footer */
.site-footer{left:0;top:1000px;width:707px;height:184px;background:var(--navy)}
.foot-col{top:1024px;color:var(--foot-text);font-size:7px;line-height:12px}
.foot-col h5{font-family:"Raleway",sans-serif;color:var(--white);font-size:9px;font-weight:700;margin-bottom:8px;letter-spacing:.3px}
.contact-row{display:flex;gap:6px;align-items:flex-start;margin-bottom:6px}
.contact-row svg{flex:none;margin-top:2px}
.social-row{display:flex;gap:7px;align-items:center;margin-bottom:7px}
.social-row i{width:14px;height:14px;border:1px solid var(--foot-text);border-radius:50%;display:block}
.post{margin-bottom:8px}
.bottom-bar{left:0;top:1184px;width:707px;height:16px;background:var(--navy-deep);color:#8fa0c0;font-size:6px;text-align:center;line-height:16px}
</style>
</head>
<body>

<header class="abs site-header">
  <span class="abs brand-name">QVD Consulting</span>
  <nav class="abs main-nav">
    <span class="active">HOME</span><span>WHY QVD?</span><span>REPORTS &amp; STUDIES</span><span>SECTORS</span><span>OUR TEAM</span>
  </nav>
  <div class="abs lang"><span class="l1"></span><span class="l2"></span></div>
</header>

<section class="abs hero" role="img" aria-label="Consultants meeting around a table in a bright office"></section>
<div class="abs hero-title">PROPERTY CONSULTING</div>
<svg class="abs hero-arrow" style="left:70px" viewBox="0 0 24 24"><path d="M15 5 8 12l7 7" stroke="#fff" stroke-width="2.5" fill="none"/></svg>
<svg class="abs hero-arrow" style="left:613px" viewBox="0 0 24 24"><path d="M9 5l7 7-7 7" stroke="#fff" stroke-width="2.5" fill="none"/></svg>

<section class="abs services"></section>
<svg class="abs notch" width="32" height="14" viewBox="0 0 32 14"><path d="M0 0h32L16 14z" fill="var(--red)"/></svg>

<div class="abs service" style="left:65px">
  <div class="service-icon"><svg width="28" height="28" viewBox="0 0 28 28" fill="none" stroke="var(--red)" stroke-width="2"><rect x="3" y="5" width="22" height="14"/><path d="M9 24l5-5 5 5"/></svg></div>
  <h3>EDUCATION<br>CONSULTATION</h3>
  <p>Class aptent taciti sociosqu ad litora<br>torquent per conubia</p>
</div>
<div class="abs service" style="left:258px">
  <div class="service-icon"><svg width="28" height="28" viewBox="0 0 28 28" fill="none" stroke="var(--red)" stroke-width="2"><rect x="7" y="4" width="14" height="21"/><path d="M11 9h2M15 9h2M11 14h2M15 14h2M11 19h2M15 19h2"/></svg></div>
  <h3>REAL ESTATE<br>CONSULTATION</h3>
  <p>Class aptent taciti sociosqu ad litora<br>torquent per conubia</p>
</div>
<div class="abs service" style="left:451px">
  <div class="service-icon"><svg width="28" height="28" viewBox="0 0 28 28" fill="none" stroke="var(--red)" stroke-width="2"><path d="M4 24h20M7 24V15M13 24V10M19 24V5"/></svg></div>
  <h3>INVESTMENT<br>CONSULTING</h3>
  <p>Class aptent taciti sociosqu ad litora<br>torquent per conubia</p>
</div>

<section class="abs why">
  <h2>WHY QVD?</h2>
  <p style="top:62px">Maecenas ut justo sed ante iaculis posuere aliquet vel mauris. Duis vel ante posuere lorem pulvinar tempus sed ac mi. Curabitur a nisl vitae orci dictum laoreet.</p>
  <p style="top:108px">Integer aliquet nisi vel nunc dictum, sed volutpat ex tincidunt. Class aptent taciti sociosqu ad litora torquent per conubia nostra. Nulla facilisi. Aenean fringilla felis in mi luctus, at pretium nisl feugiat. Sed varius justo quis lorem.</p>
  <span class="btn">LEARN MORE</span>
</section>
<div class="abs why-photo" role="img" aria-label="Two smiling business partners reviewing a tablet"></div>

<h2 class="abs reports-title">Reports &amp; Studies</h2>
<div class="abs reports-rule"></div>

<article class="abs card" style="left:72px">
  <div class="card-img" role="img" aria-label="Team discussing a report at a desk" style="background:linear-gradient(120deg,#6f6257,#b9aa98)"></div>
  <h4>Aenquent per conubia</h4>
  <p>Class aptent taciti sociosqu ad litora torquent per conubia nostra, per inceptos himenaeos.</p>
  <span class="more">READ MORE</span>
</article>
<article class="abs card" style="left:267px">
  <div class="card-img" role="img" aria-label="Colleagues in a meeting room" style="background:linear-gradient(120deg,#8a2a2a,#c8b6a6)"></div>
  <h4>Suspendisse risus nibh</h4>
  <p>Class aptent taciti sociosqu ad litora torquent per conubia nostra, per inceptos himenaeos.</p>
  <span class="more">READ MORE</span>
</article>
<article class="abs card" style="left:461px">
  <div class="card-img" role="img" aria-label="Business group reviewing charts" style="background:linear-gradient(120deg,#c5ccd2,#7f8c98)"></div>
  <h4>Etiam eleifend metus</h4>
  <p>Class aptent taciti sociosqu ad litora torquent per conubia nostra, per inceptos himenaeos.</p>
  <span class="more">READ MORE</span>
</article>

<footer class="abs site-footer"></footer>
<div class="abs foot-col" style="left:72px">
  <h5>QUICK LINKS</h5>
  Why QVD?<br>Reports &amp; Studies<br>Sectors<br>Our Team<br>Contact
</div>
<div class="abs foot-col" style="left:222px;width:150px">
  <h5>CONTACT US</h5>
  <div class="contact-row"><svg width="8" height="10" viewBox="0 0 8 10"><path d="M4 10S0 5.5 0 3.5a4 4 0 0 1 8 0C8 5.5 4 10 4 10z" fill="#cfd8ea"/></svg><span>12 Lale Sokak, Kadirga District,<br>Istanbul, Turkey</span></div>
  <div class="contact-row"><svg width="8" height="9" viewBox="0 0 8 9"><path d="M1 0h2l1 2-1 1a5 5 0 0 0 2 2l1-1 2 1v2c0 1-1 2-2 2A7 7 0 0 1 0 2C0 1 0 0 1 0z" fill="#cfd8ea"/></svg><span>+90 212 555 0148</span></div>
  <div class="contact-row"><svg width="9" height="7" viewBox="0 0 9 7"><rect width="9" height="7" fill="#cfd8ea"/><path d="M0 0l4.5 4L9 0" stroke="#0f2d63" fill="none"/></svg><span>info@qvdconsult.com</span></div>
</div>
<div class="abs foot-col" style="left:418px;width:130px">
  <h5>LATEST POSTS</h5>
  <div class="post">In iaculis facilisis lorem dictum<br>nunc quam semper<br>12 May 2024</div>
  <div class="post">Fusce tellus nisl<br>pretium ut nisi quis augue<br>08 May 2024</div>
</div>
<div class="abs foot-col" style="left:578px">
  <h5>SOCIAL</h5>
  <div class="social-row"><i></i>Community</div>
  <div class="social-row"><i></i>Updates</div>
  <div class="social-row"><i></i>Network</div>
</div>
<div class="abs bottom-bar">© 2024 QVD Consulting. All rights reserved. Terms of Use</div>

</body>
</html>
```